Sunwellflow Aquadeepflow Depot

Need a brochure to send to new prospective clients, giving them an idea of what we are and what we can do for them.
To be sent as an attachment to an email.
Printable if possible to hand out at Pastoral Expo Week.
http://www.sunwellflow.com.au/
http://www.aquadeepflow.com.au/
http://www.wellflowy.net.au/
All three of these site are part of what I do.

Target Market(s)

Rural, Sheep and cattle stations, water bore users, out of city living.

Colors
0255a3
0692cd

Requirements
Must have
• Print and email version

```html
<!DOCTYPE html>
<html lang="en">
<head>
<meta charset="utf-8">
<title>Sunwellflow Brochure</title>
<link href="https://fonts.googleapis.com/css2?family=Lato:wght@400;700&family=Oswald:wght@500;600&display=swap" rel="stylesheet">
<style>
  :root{
    --bg:#6b6b6b;
    --paper:#ffffff;
    --blue-deep:#0255a3;
    --blue-bright:#0692cd;
    --blue-light:#2aa6ea;
    --yellow:#ffd21f;
    --orange:#f6a315;
    --ink:#2b2b2b;
    --sky:#5f9fd8;
  }
  *{margin:0;padding:0;box-sizing:border-box}
  html,body{width:1200px;height:907px;overflow:hidden;background:var(--bg)}
  .brochure{position:absolute;left:120px;top:108px;width:963px;height:687px;display:flex;box-shadow:0 6px 18px rgba(0,0,0,.45)}
  .page{position:relative;height:687px;background:var(--paper);overflow:hidden}
  .page--inside{width:480px}
  .page--cover{width:483px}
  .page svg.bands{position:absolute;left:0;top:0}
  .intro{position:absolute;left:40px;top:42px;width:404px;font-family:"Lato",sans-serif;font-size:10.6px;line-height:13.4px;color:var(--ink);text-align:justify}
  .intro p{margin-bottom:12px}
  .intro strong{font-weight:700}
  .contact-label{text-transform:uppercase}
  .photo-faded{position:absolute;left:0;top:330px;width:300px;height:200px;background:linear-gradient(160deg,#f4f4f4 0%,#d9d9d9 45%,#efefef 100%)}
  .brand{position:absolute;font-family:"Oswald",sans-serif;font-weight:600;letter-spacing:.5px}
  .brand--inside{left:20px;top:612px;font-size:22px;color:#fff}
  .brand--cover{left:0;width:483px;text-align:center;top:58px;font-size:34px;color:var(--blue-deep)}
  .brand--cover .dot{display:inline-block;width:14px;height:14px;border-radius:50%;background:var(--orange);margin-right:10px;vertical-align:middle}
  .call{position:absolute;right:30px;top:545px;text-align:right;font-family:"Oswald",sans-serif;font-weight:600}
  .call-label{font-size:30px;color:var(--yellow);line-height:34px}
  .call-number{font-size:34px;color:#fff;line-height:42px}
  .call-links{position:absolute;right:30px;top:630px;text-align:right;font-family:"Lato",sans-serif;font-size:11.5px;line-height:16px;color:#fff}
  .call-links span{display:inline-block;width:10px;height:8px;border:1px solid #fff;margin-left:6px;vertical-align:middle}
  .call-links span.web{border-radius:50%;height:10px}
  .photo-main{position:absolute;left:60px;top:160px;width:382px;height:382px;border-radius:50%;border:10px solid var(--orange);background:linear-gradient(170deg,var(--sky) 0%,#9ec8ee 40%,#3a5f96 75%,#2a4a7c 100%);box-shadow:0 0 0 4px var(--yellow) inset}
  .photo-small{position:absolute;left:30px;top:402px;width:160px;height:160px;border-radius:50%;border:6px solid var(--yellow);background:linear-gradient(180deg,#6d5a3c 0%,#8a6f47 50%,#5c6b3a 100%)}
  .headline{position:absolute;left:0;width:483px;text-align:center;font-family:"Oswald",sans-serif}
  .headline-main{top:565px;font-size:46px;font-weight:600;color:var(--yellow);line-height:52px;letter-spacing:.5px}
  .headline-sub{top:618px;font-size:19px;font-weight:500;color:#fff;letter-spacing:.5px}
  .headline-url{top:646px;font-family:"Lato",sans-serif;font-size:11px;color:#fff;letter-spacing:4.5px}
</style>
</head>
<body>
<div class="brochure">
  <section class="page page--inside">
    <div class="photo-faded" role="img" aria-label="Faded photo of solar panels in a paddock"></div>
    <svg class="bands" width="480" height="687" viewBox="0 0 480 687" aria-hidden="true">
      <defs>
        <linearGradient id="blueInside" x1="0" y1="0" x2="1" y2="0">
          <stop offset="0" stop-color="var(--blue-light)"/>
          <stop offset="1" stop-color="var(--blue-deep)"/>
        </linearGradient>
      </defs>
      <path d="M0,515 C110,540 230,520 320,470 C380,438 440,428 480,440 L480,687 L0,687 Z" fill="var(--yellow)"/>
      <path d="M0,532 C120,558 240,535 330,485 C390,452 440,445 480,455 L480,687 L0,687 Z" fill="url(#blueInside)"/>
    </svg>
    <div class="intro">
      <p>At Sunwellflow we have been involved in the Drilling Industry, pumps and associated equipment in Australia and PNG since the mid 1980's. This accumulated knowledge and skill is available to share with all of our customers. Our range of products, skills and expertise is second to none.<br>We have a range of recognized formal trades incorporated in to our team including - Mechanical Trades, Licensed Water Well Drillers, Advanced Certificate in Hydraulics and Electrical Licenses. We can help you with product selection, competitive pricing, product availability, complete do it yourself kits, installation, service and advice.Send information about your bore</p>
      <p><span class="contact-label">Contact us</span><br><strong>No other company focuses soley on SOLAR WATER BORE PUMPS</strong><br><strong>Call us on 1300 555 019</strong><br>or email at <strong>info@sunwellflow.com.au.</strong></p>
      <p>Replace a windmill with a solar bore pump kit! Solar bore pumpWindmill maintenance has always been dangerous. With occupational health and safety regulations tightening, farmers need to be aware of the safety risks and their obligations.<br>Many contractors now refuse to work on windmills that are unsafe. One contractor claims that 90 per cent of the windmills he sees would not meet safety standards; so he often has to fix the frame and platform before starting work on the windmill head itself. Many farmers do not like paying contractors to fix these issues. Instead, they try to do the work themselves, without the correct safety equipment, which places them and their workers  at greater risk of injury.</p>
    </div>
    <div class="brand brand--inside">Sunwellflow</div>
    <div class="call">
      <div class="call-label">CALL US ON</div>
      <div class="call-number">1300 555 019</div>
    </div>
    <div class="call-links">info@sunwellflow.com.au.<span></span><br>www.sunwellflow.com.au.<span class="web"></span></div>
  </section>

  <section class="page page--cover">
    <svg class="bands" width="483" height="687" viewBox="0 0 483 687" aria-hidden="true">
      <defs>
        <linearGradient id="blueCover" x1="0" y1="0" x2="1" y2="0">
          <stop offset="0" stop-color="var(--blue-deep)"/>
          <stop offset=".5" stop-color="var(--blue-bright)"/>
          <stop offset="1" stop-color="var(--blue-light)"/>
        </linearGradient>
      </defs>
      <path d="M0,485 C150,505 330,505 483,465 L483,687 L0,687 Z" fill="var(--yellow)"/>
      <path d="M0,498 C160,520 330,520 483,482 L483,687 L0,687 Z" fill="url(#blueCover)"/>
    </svg>
    <div class="brand brand--cover"><span class="dot"></span>Sunwellflow</div>
    <div class="photo-main" role="img" aria-label="Photo of technicians installing solar panels on a roof under a blue sky"></div>
    <div class="photo-small" role="img" aria-label="Photo of a bore head standpipe in a paddock"></div>
    <div class="headline headline-main">FOR THE BEST VALUE</div>
    <div class="headline headline-sub">AND THE BEST ADVICE IN SOLAR BORE</div>
    <div class="headline headline-url">www.sunwellflow.com.au</div>
  </section>
</div>
</body>
</html>
```